Velmorfood

We produce juices. We need a label design for 300ml and 1L bottles. Our company's name is "Velmor food", In honor of Aragats mountain. If we like some of the examples, in future for the final result we will send Armenian version of company's name in armenian letters.

Industry/Entity Type

It Company

```html
<!DOCTYPE html>
<html lang="en">
<head>
<meta charset="UTF-8">
<title>Velmor food — Strawberry Juice Label</title>
<link rel="stylesheet" href="https://fonts.googleapis.com/css2?family=Nunito:wght@300;800&family=Comfortaa:wght@500&display=swap">
<style>
  :root {
    --juice-red: #ea4a43;
    --juice-red-deep: #dc3b36;
    --juice-red-light: #f2675d;
    --label-white: #ffffff;
    --accent-lime: #d8e23a;
  }
  html, body {
    margin: 0;
    padding: 0;
    width: 1200px;
    height: 2636px;
    overflow: hidden;
  }
  .label {
    position: relative;
    width: 1200px;
    height: 2636px;
    background: linear-gradient(180deg, var(--juice-red-light) 0%, var(--juice-red) 45%, var(--juice-red-deep) 100%);
    overflow: hidden;
  }
  .brand {
    position: absolute;
    left: 560px;
    top: 360px;
    display: flex;
    align-items: center;
    gap: 22px;
  }
  .brand-dot {
    width: 34px;
    height: 34px;
    border-radius: 50%;
    background: var(--accent-lime);
    flex: none;
  }
  .brand-name {
    font-family: "Comfortaa", sans-serif;
    font-weight: 500;
    font-size: 62px;
    line-height: 1;
    color: var(--accent-lime);
    white-space: nowrap;
  }
  .flavour {
    position: absolute;
    left: 220px;
    top: 990px;
    width: 780px;
    height: 420px;
    margin: 0;
    transform: rotate(-90deg);
    transform-origin: center center;
    font-family: "Nunito", sans-serif;
    font-weight: 800;
    font-size: 250px;
    line-height: 210px;
    letter-spacing: -6px;
    color: var(--label-white);
    text-align: left;
  }
  .flavour span {
    display: block;
  }
  .product-type {
    position: absolute;
    left: 0;
    width: 1120px;
    top: 1620px;
    margin: 0;
    text-align: center;
    font-family: "Nunito", sans-serif;
    font-weight: 300;
    font-size: 78px;
    line-height: 1;
    color: var(--accent-lime);
  }
</style>
</head>
<body>
  <main class="label">
    <div class="brand">
      <span class="brand-dot"></span>
      <span class="brand-name">Velmor food</span>
    </div>
    <h1 class="flavour"><span>straw</span><span>berry</span></h1>
    <p class="product-type">juice</p>
  </main>
</body>
</html>
```